Ridgeway Framers Business Card

I'm looking for a business card design for a start-up Handyman/Construction Company. The organization will double as a ministry to the homeless, hoping to create job opportunity and training to the homeless, providing a pathway back to being "homed". I'm looking for a simple to "seeming" simple design. Open to all thoughts.

Industry/Entity Type

Ministry

Requirements
Must have
• Logo (Attached), Name, Phone, Email and Address. Note - "*Registered and Insured".

```html
<!DOCTYPE html>
<html lang="en">
<head>
<meta charset="utf-8">
<title>Ridgeway Framers Business Card</title>
<link rel="stylesheet" href="https://fonts.googleapis.com/css2?family=Josefin+Sans:wght@400;700&family=Montserrat:wght@400;600;700&display=swap">
<style>
  :root {
    --page-bg: #e9e7e4;
    --card-white: #ffffff;
    --card-slate: #3b4451;
    --ink-slate: #3a4350;
    --accent-purple: #7b2d8e;
    --lilac-light: #d9bfe3;
    --lilac-mid: #b58bc6;
    --text-light: #f2f2f2;
    --text-muted: #c9ced6;
  }
  * { margin: 0; padding: 0; box-sizing: border-box; }
  html, body { width: 1200px; height: 900px; overflow: hidden; }
  body {
    background: var(--page-bg);
    font-family: "Montserrat", Arial, sans-serif;
    position: relative;
  }
  .card {
    position: absolute;
    left: 320px;
    width: 560px;
    height: 300px;
    box-shadow: 0 10px 24px rgba(0,0,0,0.25);
    overflow: hidden;
  }
  /* Front card */
  .card-front { top: 110px; background: var(--card-white); }
  .cross-field {
    position: absolute;
    left: 14px; top: 36px;
    width: 230px; height: 240px;
    background: radial-gradient(ellipse at 45% 40%, var(--lilac-mid) 0%, var(--lilac-light) 55%, var(--card-white) 85%);
  }
  .front-brand {
    position: absolute;
    left: 262px; top: 108px;
  }
  .brand-name {
    font-family: "Josefin Sans", Arial, sans-serif;
    font-weight: 700;
    color: var(--ink-slate);
    font-size: 32px;
    letter-spacing: 0.5px;
    line-height: 1;
  }
  .front-note {
    margin-top: 14px;
    font-size: 11.5px;
    font-weight: 700;
    letter-spacing: 1.6px;
    color: var(--ink-slate);
  }
  /* Back card */
  .card-back { top: 470px; background: var(--card-slate); }
  .back-brand {
    position: absolute;
    left: 36px; top: 40px;
  }
  .back-brand .brand-name { color: var(--text-light); font-size: 38px; }
  .divider {
    position: absolute;
    left: 36px; top: 146px;
    width: 488px; height: 4px;
    background: var(--text-light);
    border-radius: 2px;
  }
  .person {
    position: absolute;
    right: 60px; top: 134px;
    background: var(--card-slate);
    padding: 0 10px;
  }
  .person-name {
    font-family: "Josefin Sans", Arial, sans-serif;
    font-weight: 700;
    font-size: 18px;
    letter-spacing: 1px;
    color: var(--text-light);
  }
  .person-role {
    font-size: 11px;
    color: var(--text-muted);
    margin-top: 2px;
  }
  .contact-list {
    position: absolute;
    left: 36px; top: 206px;
    list-style: none;
    font-size: 12px;
    color: var(--text-light);
  }
  .contact-list li { display: flex; align-items: center; gap: 6px; margin-bottom: 7px; }
  .contact-list svg { width: 13px; height: 13px; }
  .address {
    position: absolute;
    right: 44px; top: 216px;
    text-align: right;
    font-size: 11.5px;
    font-weight: 700;
    letter-spacing: 0.6px;
    line-height: 1.55;
    color: var(--text-light);
  }
  .accent-band {
    position: absolute;
    left: 0; bottom: 18px;
    width: 100%; height: 12px;
    background: var(--accent-purple);
  }
</style>
</head>
<body>
  <section class="card card-front">
    <div class="cross-field" role="img" aria-label="Decorative field of scattered lilac cross marks"></div>
    <div class="front-brand">
      <div class="brand-name">Ridgeway Framers</div>
      <div class="front-note">REGISTERED AND INSURED</div>
    </div>
  </section>

  <section class="card card-back">
    <div class="back-brand">
      <div class="brand-name">Ridgeway Framers</div>
    </div>
    <div class="divider"></div>
    <div class="person">
      <div class="person-name">DANA MORROW</div>
      <div class="person-role">Director</div>
    </div>
    <ul class="contact-list">
      <li>
        <svg viewBox="0 0 16 16" aria-hidden="true"><circle cx="8" cy="8" r="7.5" fill="#f2f2f2"/><path d="M5.2 4.2l1.6 0 .7 2-1 .8a5 5 0 0 0 2.5 2.5l.8-1 2 .7 0 1.6c-3.8.3-6.9-2.8-6.6-6.6z" fill="#3b4451"/></svg>
        <span>0144 782 305</span>
      </li>
      <li>
        <svg viewBox="0 0 16 16" aria-hidden="true"><circle cx="8" cy="8" r="7.5" fill="#f2f2f2"/><rect x="4" y="5.2" width="8" height="5.6" fill="#3b4451"/><path d="M4 5.2l4 3 4-3" stroke="#f2f2f2" stroke-width="0.9" fill="none"/></svg>
        <span>dana@ridgewayframers.com</span>
      </li>
    </ul>
    <div class="address">418, LARCHMONT ROAD<br>FAIRVIEW, ANY CITY</div>
    <div class="accent-band"></div>
  </section>
</body>
</html>
```